Marlo Tidy Yard Website

We need a website design for this new company. I've attached the company logo. This company is in the construction industry that provides general labor, maintenance and cleaning for construction sites. We want a clean and simple website that can be easy to navigate.

Target Market(s)

Construction industry

Industry/Entity Type

Construction

Number of Pages Required

2 page

Font styles to use
Sans Serif

```html
<!DOCTYPE html>
<html lang="en">
<head>
<meta charset="utf-8">
<title>Marlo Tidy Yard</title>
<link href="https://fonts.googleapis.com/css2?family=Montserrat:wght@400;500;600;700;800&family=Open+Sans:wght@400;600&display=swap" rel="stylesheet">
<style>
:root{
  --orange:#f15a1f;
  --navy:#1b1f5e;
  --ink:#222;
  --body:#444;
  --muted:#666;
  --light:#f3f3f3;
  --footer:#1e1e1e;
  --line:#dcdcdc;
}
*{margin:0;padding:0;box-sizing:border-box}
html,body{width:1200px;height:3130px;overflow:hidden;background:#fff}
body{position:relative;font-family:"Open Sans",Arial,sans-serif;color:var(--body)}
.abs{position:absolute}
h1,h2,h3,h4,.nav a,.brand{font-family:"Montserrat",Arial,sans-serif}

/* header */
.topbar{left:660px;top:0;width:540px;height:44px;background:var(--orange);clip-path:polygon(0 0,100% 0,100% 100%,28px 100%);color:#fff;font-size:13px;display:flex;align-items:center;gap:26px;padding-left:34px;font-family:"Montserrat",sans-serif}
.topbar span{display:flex;align-items:center;gap:8px}
.brand-head{left:112px;top:24px;width:160px;font-weight:800;color:var(--navy);font-size:30px;line-height:30px;letter-spacing:-.5px}
.nav{top:80px;left:465px;display:flex;gap:0}
.nav a{font-size:13px;font-weight:600;color:#222;text-decoration:none;text-transform:uppercase;position:absolute;white-space:nowrap}
.nav a.active{color:var(--orange)}

/* hero */
.hero-photo{left:0;top:128px;width:1200px;height:600px;background:linear-gradient(180deg,#5f7ea6 0%,#9cb3c9 30%,#d3a273 62%,#7b4a2a 100%)}
.hero-name{left:272px;top:165px;font-family:"Montserrat",sans-serif;font-weight:700;color:rgba(255,255,255,.35);font-size:70px;line-height:82px}
.hero-curve{left:0;top:500px}
.blueprint{left:0;top:740px;width:1200px;height:630px;background:linear-gradient(180deg,#fafafa,#f3f4f6)}

/* sections */
.section-title{width:1200px;text-align:center;font-family:"Montserrat",sans-serif;font-weight:500;color:var(--navy);font-size:36px;letter-spacing:.5px}
.section-sub{width:1200px;text-align:center;font-size:12.5px;color:var(--body)}

.service-card{width:440px;height:436px;background:#fff;border:1px solid var(--line)}
.service-img{position:absolute;left:0;top:0;width:100%;height:243px}
.service-icon{position:absolute;left:169px;top:193px;width:100px;height:100px;border-radius:50%;background:var(--orange);border:5px solid #fff;display:flex;align-items:center;justify-content:center}
.service-card h3{position:absolute;top:304px;width:100%;text-align:center;font-weight:500;font-size:17px;color:var(--ink);letter-spacing:.5px}
.service-card p{position:absolute;top:342px;left:45px;right:45px;text-align:center;font-size:12.5px;line-height:25px;color:var(--body)}

.whatwedo{left:0;top:1373px;width:1200px;height:507px;background:linear-gradient(90deg,#dde6ef 0%,#cfdbe7 45%,#8fa6be 62%,#5d7290 80%,#c98a3a 100%)}
.whatwedo h2{position:absolute;left:113px;top:115px;font-weight:500;font-size:42px;color:var(--navy);letter-spacing:.5px}
.whatwedo p{position:absolute;left:113px;top:188px;width:430px;font-size:12.5px;line-height:28px;color:#333}
.btn-navy{position:absolute;left:113px;top:357px;width:160px;height:53px;border-radius:27px;background:var(--navy);color:#fff;font-family:"Montserrat",sans-serif;font-weight:600;font-size:15px;display:flex;align-items:center;justify-content:center}

.blog-img{width:306px;height:212px}
.date{position:absolute;left:12px;top:17px;width:48px;height:55px;background:var(--orange);color:#fff;text-align:center;font-family:"Montserrat",sans-serif;line-height:1}
.date b{display:block;font-size:22px;font-weight:500;margin-top:7px}
.date small{font-size:10px}
.blog-box{width:270px;height:158px;background:#fff;border:1px solid var(--line);border-top:none}
.blog-box h4{position:absolute;top:18px;width:100%;text-align:center;font-size:13px;font-weight:600;color:#222}
.blog-box p{position:absolute;top:48px;left:18px;right:14px;font-size:12px;line-height:24px;color:var(--body)}
.btn-outline{position:absolute;width:118px;height:41px;border:2px solid var(--orange);color:var(--orange);font-family:"Montserrat",sans-serif;font-size:14px;font-weight:500;display:flex;align-items:center;justify-content:center;background:#fff}

.testimonials{left:0;top:2462px;width:1200px;height:260px;background:var(--light)}
.avatar{position:absolute;width:132px;height:132px;border-radius:50%;background:linear-gradient(160deg,#c9c9c9,#7a6a5e);border:4px solid #fff;box-shadow:0 0 0 2px #ccc}
.divider{position:absolute;width:1px;height:150px;background:#bbb}
.quote{position:absolute;width:300px;font-size:12.5px;line-height:26px;color:#333}
.quote i{color:var(--orange);font-style:normal;font-family:Georgia,serif;font-size:30px;font-weight:700;line-height:10px;vertical-align:-6px;margin-right:4px}
.author{position:absolute;font-size:13px;color:#333;font-family:"Montserrat",sans-serif}
.stars{position:absolute;font-size:14px;letter-spacing:1px;color:#888}
.stars b{color:var(--orange);font-weight:400}

.footer{left:0;top:2722px;width:1200px;height:408px;background:var(--footer);color:#fff}
.footer-brand{position:absolute;left:155px;top:92px;font-family:"Montserrat",sans-serif;font-weight:800;font-size:48px;line-height:58px;color:#fff;letter-spacing:-.5px}
.footer h3{position:absolute;font-weight:500;font-size:26px;letter-spacing:.5px}
.address{position:absolute;left:492px;top:100px;font-size:13px;line-height:19px}
.address dt{margin-top:18px}
.address dt:first-child{margin-top:0}
.field{position:absolute;left:745px;width:283px;height:36px;background:#fff;color:#444;font-size:12px;padding:9px 14px}
.submit{position:absolute;left:745px;top:268px;width:90px;height:34px;background:var(--orange);color:#fff;font-family:"Montserrat",sans-serif;font-weight:600;font-size:13px;display:flex;align-items:center;justify-content:center}
.copyright{position:absolute;top:358px;width:100%;text-align:center;font-size:13px;color:#ddd}
</style>
</head>
<body>

<header>
  <div class="abs topbar">
    <span>
      <svg width="13" height="13" viewBox="0 0 24 24" fill="#fff"><path d="M6.6 10.8c1.4 2.8 3.8 5.1 6.6 6.6l2.2-2.2c.3-.3.7-.4 1-.2 1.1.4 2.3.6 3.6.6.6 0 1 .4 1 1V20c0 .6-.4 1-1 1C10.6 21 3 13.4 3 4c0-.6.4-1 1-1h3.5c.6 0 1 .4 1 1 0 1.3.2 2.5.6 3.6.1.3 0 .7-.2 1z"/></svg>
      CALL US : 000-484-2270
    </span>
    <span>
      <svg width="14" height="11" viewBox="0 0 24 18" fill="#fff"><path d="M0 0h24v18H0z" fill="none"/><path d="M2 0h20a2 2 0 0 1 2 2v.5L12 10 0 2.5V2a2 2 0 0 1 2-2zm22 5v11a2 2 0 0 1-2 2H2a2 2 0 0 1-2-2V5l12 7.5z"/></svg>
      EMAIL : info@marlotidyyard.com
    </span>
  </div>
  <div class="abs brand brand-head">MARLO TIDY YARD</div>
  <nav class="abs nav">
    <a class="active" href="#" style="left:0">Home</a>
    <a href="#" style="left:89px">About Us</a>
    <a href="#" style="left:205px">Services</a>
    <a href="#" style="left:315px">News</a>
    <a href="#" style="left:405px">Testimonials</a>
    <a href="#" style="left:545px">Contact Us</a>
  </nav>
</header>

<section class="hero">
  <div class="abs hero-photo" role="img" aria-label="Industrial plant with chimneys and lights at dusk by the sea"></div>
  <div class="abs hero-name">MARLO<br>TIDY YARD</div>
  <div class="abs blueprint"></div>
  <svg class="abs hero-curve" width="1200" height="260" viewBox="0 0 1200 260">
    <path d="M0 62 C320 20 640 110 1200 125 L1200 240 L0 240 Z" fill="#fff"/>
    <path d="M0 62 C320 20 640 110 1200 125 L1200 232 C860 232 460 150 0 78 Z" fill="#f15a1f"/>
    <path d="M0 78 C460 150 860 232 1200 232" fill="none" stroke="#fff" stroke-width="6"/>
    <path d="M0 88 C460 165 860 248 1200 248" fill="none" stroke="#9b9b9b" stroke-width="6"/>
  </svg>
</section>

<section class="services">
  <h2 class="abs section-title" style="top:760px">OUR SERVICES</h2>
  <p class="abs section-sub" style="top:836px">Sed ut perspiciatis unde omnis iste natus error sit voluptatem accusantium doloremque laudantium, totam rem aperiam</p>

  <article class="abs service-card" style="left:138px;top:882px">
    <div class="service-img" role="img" aria-label="Two workers in hard hats and safety vests on a site" style="background:linear-gradient(135deg,#f2a06a,#d9c0b3 45%,#5d6473)"></div>
    <div class="service-icon">
      <svg width="48" height="48" viewBox="0 0 48 48" fill="none" stroke="#fff" stroke-width="4" stroke-linecap="round">
        <path d="M10 38 L30 18"/><path d="M30 18 a7 7 0 1 0 6 -10 l-4 4 -3 -1 -1 -3 4 -4"/>
        <path d="M12 10 L38 36"/><path d="M8 6 l6 2 -2 2 z"/>
      </svg>
    </div>
    <h3>MAINTENANCE</h3>
    <p>Sed ut perspiciatis unde omnis iste natus error sit voluptatem accusan tium doloremque laudantium, totam rem aperiam, eaque ipsa quae ab illo inventore veritatis</p>
  </article>

  <article class="abs service-card" style="left:622px;top:882px">
    <div class="service-img" role="img" aria-label="Cleaner in white overalls using an industrial vacuum" style="background:linear-gradient(135deg,#c9c4bd,#8f8b86 50%,#3c4a74)"></div>
    <div class="service-icon">
      <svg width="48" height="48" viewBox="0 0 48 48" fill="none" stroke="#fff" stroke-width="3.5" stroke-linecap="round" stroke-linejoin="round">
        <path d="M30 6 C20 6 22 20 14 24"/>
        <path d="M8 40 V32 a8 8 0 0 1 16 0 v8 z"/>
        <path d="M24 40 h16"/><circle cx="12" cy="42" r="2"/>
      </svg>
    </div>
    <h3>CLEANING SERVICES</h3>
    <p>Sed ut perspiciatis unde omnis iste natus error sit voluptatem accusan tium doloremque laudantium, totam rem aperiam, eaque ipsa quae ab illo inventore veritatis</p>
  </article>
</section>

<section class="abs whatwedo" role="img" aria-label="Refinery towers blended with a worker holding an orange hard hat">
  <h2>WHAT WE DO</h2>
  <p>Sed ut perspiciatis unde omnis iste natus error sit voluptatem accusantium dolor em que laudantium, totam rem aperiam, eaque ipsa quae ab illo inventore veritatis et quasi architecto beatae vitae dicta sunt explicabo. Nemo enim ipsam voluptatem quia voluptas sit aspernatur aut odit aut fugit, sed quia consequuntur dolores eos qui ratione voluptatem sequi nesciunt.</p>
  <div class="btn-navy">READ MORE</div>
</section>

<section class="blog">
  <h2 class="abs section-title" style="top:1916px">LATEST BLOG</h2>
  <p class="abs section-sub" style="top:1990px">Sed ut perspiciatis unde omnis iste natus error sit voluptatem accusantium doloremque laudantium, totam rem aperiam</p>

  <div class="abs blog-img" style="left:113px;top:2043px;background:linear-gradient(180deg,#5b6fa8,#c27a9a 50%,#2e2b3a)" role="img" aria-label="Industrial harbour at sunset with a mountain behind"><div class="date"><b>02</b><small>JAN</small></div></div>
  <div class="abs blog-box" style="left:130px;top:2225px"><h4>SED UT PERSPICIATIS UNDE OMNIS</h4><p>Sed ut perspiciatis unde omnis iste natus err or sit voluptatem accusantium dolorem vitae dicta sunt explicabo.</p></div>
  <div class="btn-outline" style="left:206px;top:2362px">READ MORE</div>

  <div class="abs blog-img" style="left:446px;top:2043px;background:linear-gradient(160deg,#3a3f46,#6a5c4c 55%,#d2762e)" role="img" aria-label="Welder at work with sparks flying"><div class="date"><b>02</b><small>JAN</small></div></div>
  <div class="abs blog-box" style="left:464px;top:2225px"><h4>SED UT PERSPICIATIS UNDE OMNIS</h4><p>Sed ut perspiciatis unde omnis iste natus err or sit voluptatem accusantium dolorem vitae dicta sunt explicabo.</p></div>
  <div class="btn-outline" style="left:540px;top:2362px">READ MORE</div>

  <div class="abs blog-img" style="left:781px;top:2043px;background:linear-gradient(180deg,#2f6fcf,#8fb6e6 55%,#4d5563)" role="img" aria-label="Modern warehouse building under blue sky"><div class="date"><b>02</b><small>JAN</small></div></div>
  <div class="abs blog-box" style="left:799px;top:2225px"><h4>SED UT PERSPICIATIS UNDE OMNIS</h4><p>Sed ut perspiciatis unde omnis iste natus err or sit voluptatem accusantium dolorem vitae dicta sunt explicabo.</p></div>
  <div class="btn-outline" style="left:875px;top:2362px">READ MORE</div>
</section>

<section class="abs testimonials">
  <div class="avatar" style="left:117px;top:54px" role="img" aria-label="Portrait of a client"></div>
  <div class="divider" style="left:263px;top:45px"></div>
  <p class="quote" style="left:287px;top:58px"><i>“</i>Sed ut perspiciatis unde omnis iste natus error sit voluptatem accusantium doloremque laudantium, totam rem aperiam, eaque ipsa quae ab illo inventore veritatis et quasi architecto beatae vitae dicta sunt explicabo.</p>
  <div class="author" style="left:287px;top:182px">- RAVI DENHOLM</div>
  <div class="stars" style="left:513px;top:180px"><b>★★★</b>★★</div>

  <div class="avatar" style="left:622px;top:54px" role="img" aria-label="Portrait of a client"></div>
  <div class="divider" style="left:770px;top:45px"></div>
  <p class="quote" style="left:793px;top:58px"><i>“</i>Sed ut perspiciatis unde omnis iste natus error sit voluptatem accusantium doloremque laudantium, totam rem aperiam, eaque ipsa quae ab illo inventore veritatis et quasi architecto beatae vitae dicta sunt explicabo.</p>
  <div class="author" style="left:793px;top:182px">- RAVI DENHOLM</div>
  <div class="stars" style="left:1018px;top:180px"><b>★★★</b>★★</div>
</section>

<footer class="abs footer">
  <div class="footer-brand">MARLO<br>TIDY YARD</div>

  <h3 style="left:492px;top:42px">ADDRESS</h3>
  <dl class="address">
    <dt>ADDRESS</dt><dd># 245 Lorem Ipsum DUmmy<br>Lorem Ipsum</dd>
    <dt>PHONE</dt><dd>(000)-484-2270</dd>
    <dt>EMAIL</dt><dd>info@marlotidyyard.com</dd>
  </dl>

  <h3 style="left:745px;top:42px">CONTACT FORM</h3>
  <div class="field" style="top:90px">Name :</div>
  <div class="field" style="top:130px">Email :</div>
  <div class="field" style="top:170px">Subject :</div>
  <div class="field" style="top:210px;height:46px">Message :</div>
  <div class="submit">SUBMIT</div>

  <p class="copyright">© Copyright 2019 Marlo Tidy Yard.All right reserved</p>
</footer>

</body>
</html>
```